Career development coaching - school lever to adults, needs a business card

Tandel Grove - An independent Career Advice business that provides 1-2-1 advice,for career development, entrepreneurial support and workshops needs a business card. Our clients of all ages (school leaver to adults looking for a career move) and universities and colleges. We would like the card to be double-sided with a modern, professional look. Looking for something professional yet very creative and original. Want a standard size business card that inspires a second look because it stands out from the rest.

One side of the card to have a design incorporating the logo with Tandel Grove name with the strap line “Helping you find your future” and space for the company website

Other side of the card to the logo/Tandel Grove name and the usual contact information:
Individual Name
Job Title (for example, Director)
Phone number
Email address
Company website address

Facebook, LinkedIn and Twitter links will need to go somewhere (back or front!)

The design will be used for 3 individuals so should be editable so that we can update as needed/as we grow.

Attached is the company logo/colours to be incorporated.

Target Market(s)

1-2-1 advice,for career development, entrepreneurial support and workshops needs a business card. Our clients of all ages (school leaver to adults looking for a career move) and universities and colleges.

Industry/Entity Type

Consulting

Contact Information for Business Card

Individual Name
Phone number
Email address
Company website address

Font styles to use
Sans Serif

Colors
0255a3
3176b5
faa54b
f78f20
85acd3
cfdeed

Requirements
Must have
• use the Tandel Grove Logo in some way - using the colours and the blue/orange palette
• For the logo - hope this makes sense to someone or if they direclty relate to the logo image attached!
• For the Orange:- Pantone 1585 C
• In CMYK : C3 M71 Y100 K0
• For the Blue:- 100% Pantone 7469 C
• In CMYK : C100 M62 Y27 K7
• Please feel free to contact me with any questions for more info
Nice to have
• happy to see any creative designs
Should not have
• Nothing too traditional,

```html
<!DOCTYPE html>
<html lang="en">
<head>
<meta charset="utf-8">
<title>Tandel Grove – Business Card</title>
<link href="https://fonts.googleapis.com/css2?family=Open+Sans:wght@400;600;700;800&display=swap" rel="stylesheet">
<style>
  :root {
    --blue: #0a5e94;
    --blue-deep: #02528a;
    --blue-light: #1a7ab2;
    --orange: #f7762b;
    --white: #ffffff;
    --backdrop: #bcbcbc;
    --ink-shadow: rgba(0, 0, 0, 0.22);
  }
  * { box-sizing: border-box; margin: 0; padding: 0; }
  html, body {
    width: 1200px; height: 800px; overflow: hidden;
    background: var(--backdrop);
    font-family: "Open Sans", Arial, sans-serif;
  }
  .sheet {
    position: relative; width: 1200px; height: 800px;
    display: flex; align-items: center; justify-content: center; gap: 40px;
  }
  .card {
    position: relative; width: 540px; height: 309px; overflow: hidden;
    box-shadow: 0 10px 24px var(--ink-shadow);
  }

  /* Contact side */
  .card--contact { background: var(--white); }
  .card--contact .edge-band {
    position: absolute; top: 0; right: 0; width: 58px; height: 100%;
    background: var(--orange);
  }
  .card--contact .edge-band::before {
    content: ""; position: absolute; top: 0; left: -18px; width: 10px; height: 100%;
    background: var(--blue);
  }
  .brand {
    position: absolute; display: flex; align-items: center; gap: 10px;
    font-weight: 700; letter-spacing: 0.04em; text-transform: uppercase;
  }
  .brand__dot { width: 18px; height: 18px; border-radius: 50%; flex: none; }
  .card--contact .brand { top: 38px; left: 40px; font-size: 24px; color: var(--blue); }
  .card--contact .brand__dot { background: var(--orange); }

  .person { position: absolute; top: 108px; left: 40px; }
  .person__name {
    font-size: 21px; font-weight: 700; color: var(--orange);
    text-transform: uppercase; line-height: 1.1;
  }
  .person__role { font-size: 14px; font-weight: 600; color: var(--blue); margin-bottom: 16px; }
  .contact-list { list-style: none; }
  .contact-list li {
    display: flex; align-items: center; gap: 10px;
    font-size: 14px; font-weight: 600; color: var(--blue); line-height: 1.75;
  }
  .contact-list .icon {
    width: 18px; height: 18px; background: var(--orange); border-radius: 2px;
    display: flex; align-items: center; justify-content: center; flex: none;
  }

  /* Brand side */
  .card--brand {
    background: linear-gradient(120deg, var(--blue-deep) 0%, var(--blue) 55%, var(--blue-light) 100%);
    color: var(--white);
  }
  .tagline {
    position: absolute; top: 40px; right: 36px;
    font-size: 15px; font-weight: 700; letter-spacing: 0.08em; text-transform: uppercase;
  }
  .card--brand .brand { right: 36px; bottom: 40px; font-size: 24px; color: var(--white); }
  .card--brand .brand__dot { background: var(--white); }
</style>
</head>
<body>
<main class="sheet">
  <section class="card card--contact" aria-label="Business card, contact side">
    <div class="edge-band"></div>
    <div class="brand"><span class="brand__dot"></span>Tandel Grove</div>
    <div class="person">
      <p class="person__name">Nora Pell</p>
      <p class="person__role">Manager</p>
      <ul class="contact-list">
        <li>
          <span class="icon"><svg width="12" height="12" viewBox="0 0 24 24" aria-hidden="true"><path fill="#fff" d="M6.6 10.8a15 15 0 0 0 6.6 6.6l2.2-2.2a1 1 0 0 1 1-.25 11.4 11.4 0 0 0 3.6.57 1 1 0 0 1 1 1V20a1 1 0 0 1-1 1A17 17 0 0 1 3 4a1 1 0 0 1 1-1h3.5a1 1 0 0 1 1 1c0 1.25.2 2.45.57 3.57a1 1 0 0 1-.25 1z"/></svg></span>
          555 204 7316
        </li>
        <li>
          <span class="icon"><svg width="12" height="12" viewBox="0 0 24 24" aria-hidden="true"><path fill="none" stroke="#fff" stroke-width="2.4" d="M3 6h18v12H3z M3 6l9 7 9-7"/></svg></span>
          hello@tandelgrove.com
        </li>
        <li>
          <span class="icon"><svg width="12" height="12" viewBox="0 0 24 24" aria-hidden="true"><g fill="none" stroke="#fff" stroke-width="2.2"><circle cx="12" cy="12" r="9"/><path d="M3 12h18M12 3c3 3 3 15 0 18M12 3c-3 3-3 15 0 18"/></g></svg></span>
          www.tandelgrove.com
        </li>
      </ul>
    </div>
  </section>

  <section class="card card--brand" aria-label="Business card, brand side">
    <p class="tagline">Helping you find your future</p>
    <div class="brand"><span class="brand__dot"></span>Tandel Grove</div>
  </section>
</main>
</body>
</html>
```